Need Power Point Presentation - That incorporates New Logo

We have a new logo and would like to incorporate it into a Power Point template. We are looking for title page, 2 body pages and a closing page design. If you have any questions please let me know. New logo is attached.

```html
<!DOCTYPE html>
<html lang="en">
<head>
<meta charset="utf-8">
<title>Norvane Presentation Template</title>
<link rel="stylesheet" href="https://fonts.googleapis.com/css2?family=Carlito&family=Marcellus&display=swap">
<style>
  :root {
    --stage-light: #f7fafc;
    --stage-blue: #a9d3ec;
    --slide-white: #ffffff;
    --slide-tint: #d6ebf7;
    --brand-blue: #48ace0;
    --ribbon-deep: #8ccbeb;
    --ribbon-soft: #cbe6f5;
    --text-dark: #1a1a1a;
    --text-muted: #8a8f94;
    --frame-line: #9aa3aa;
  }
  * { box-sizing: border-box; margin: 0; padding: 0; }
  html, body { width: 1200px; height: 900px; overflow: hidden; }
  body {
    position: relative;
    background: radial-gradient(ellipse at 25% 30%, var(--stage-light) 0%, #eef5fa 45%, var(--stage-blue) 100%);
    font-family: "Carlito", "Calibri", sans-serif;
    color: var(--text-dark);
  }
  .slide {
    position: absolute;
    width: 435px; height: 326px;
    overflow: hidden;
    background: radial-gradient(ellipse at 35% 35%, var(--slide-white) 0%, #f2f8fc 55%, var(--slide-tint) 100%);
    box-shadow: 0 2px 8px rgba(40, 70, 100, 0.35);
  }
  .slide--title   { left: 123px; top: 87px; }
  .slide--content { left: 643px; top: 87px; }
  .slide--list    { left: 123px; top: 487px; }
  .slide--closing { left: 643px; top: 487px; }

  .ribbons {
    position: absolute; top: 0; height: 100%;
  }
  .ribbons--right {
    right: 0; width: 150px;
    background: linear-gradient(100deg, rgba(140,203,235,0) 0%, var(--ribbon-soft) 30%, var(--ribbon-deep) 65%, var(--ribbon-soft) 100%);
    border-top-left-radius: 120px 200px;
  }
  .ribbons--left {
    left: 0; width: 140px;
    background: linear-gradient(260deg, rgba(140,203,235,0) 0%, var(--ribbon-soft) 30%, var(--ribbon-deep) 65%, var(--ribbon-soft) 100%);
    border-bottom-right-radius: 120px 220px;
  }

  .placeholder {
    position: absolute;
    border: 1px dashed var(--frame-line);
  }
  .brand {
    position: absolute;
    display: flex; align-items: center; gap: 8px;
    font-family: "Marcellus", "Trajan Pro", serif;
    color: var(--brand-blue);
    letter-spacing: 1px;
  }
  .brand__dot { border-radius: 50%; background: var(--brand-blue); }
  .brand--large { left: 34px; top: 32px; font-size: 36px; }
  .brand--large .brand__dot { width: 22px; height: 22px; }
  .brand--small { right: 10px; bottom: 14px; font-size: 22px; gap: 5px; }
  .brand--small .brand__dot { width: 14px; height: 14px; }

  .title-box { left: 32px; top: 112px; width: 256px; height: 70px;
    display: flex; align-items: center; justify-content: center; font-size: 24px; }
  .overview-box { left: 32px; top: 191px; width: 256px; height: 121px;
    text-align: center; font-size: 18px; color: var(--text-muted); padding-top: 4px; line-height: 1.2; }

  .slide-title-box { left: 152px; top: 12px; width: 262px; height: 56px;
    display: flex; align-items: center; justify-content: center; font-size: 24px; }
  .body-box { padding: 4px 0 0 4px; }
  .content-box { left: 152px; top: 75px; width: 262px; height: 217px; }
  .list-box { left: 22px; top: 12px; width: 244px; height: 280px; }
  .closing-box { left: 130px; top: 118px; width: 277px; height: 153px; font-size: 17px; }

  .bullets { list-style: none; font-size: 17px; }
  .bullets li { padding-left: 16px; position: relative; }
  .bullets li::before { content: "•"; position: absolute; left: 2px; }
  .bullets .sub { font-size: 15px; padding-left: 38px; margin-top: 3px; }
  .bullets .sub::before { content: "–"; left: 26px; }

  .insert-icons {
    position: absolute; left: 50%; top: 50%;
    transform: translate(-50%, -50%);
  }
  .content-box .insert-icons { top: 52%; }
  .list-box .insert-icons { top: 50%; }
  .closing-box .insert-icons { top: 55%; }

  .thanks {
    position: absolute; left: 128px; top: 58px;
    font-family: "Marcellus", "Trajan Pro", serif;
    font-size: 42px; color: var(--brand-blue);
    text-shadow: 1px 2px 2px rgba(60, 80, 100, 0.35);
    letter-spacing: 0.5px;
  }
</style>
</head>
<body>

<section class="slide slide--title">
  <div class="ribbons ribbons--right" role="img" aria-label="Flowing blue ribbon decoration"></div>
  <div class="brand brand--large"><span class="brand__dot"></span>NORVANE</div>
  <div class="placeholder title-box">Presentation Title</div>
  <div class="placeholder overview-box">Brief presentation overview<br>(optional)</div>
</section>

<section class="slide slide--content">
  <div class="ribbons ribbons--left" role="img" aria-label="Flowing blue ribbon decoration"></div>
  <div class="placeholder slide-title-box">Slide Title</div>
  <div class="placeholder body-box content-box">
    <ul class="bullets">
      <li>General Content</li>
      <li class="sub">Specific Content</li>
    </ul>
    <svg class="insert-icons" width="52" height="34" viewBox="0 0 52 34" aria-hidden="true">
      <rect x="1" y="1" width="14" height="13" fill="#cfdbe6" stroke="#7f97ad"/>
      <rect x="19" y="4" width="4" height="10" fill="#e0803a"/><rect x="24" y="1" width="4" height="13" fill="#4f8fd0"/><rect x="29" y="6" width="4" height="8" fill="#8fbf4a"/>
      <rect x="37" y="2" width="14" height="12" fill="#b9d89a" stroke="#7aa55a"/>
      <rect x="1" y="19" width="14" height="13" fill="#d6e6f3" stroke="#7f97ad"/>
      <rect x="19" y="19" width="14" height="13" fill="#e9d48a" stroke="#a99450"/>
      <circle cx="44" cy="26" r="6" fill="#c9d3dc" stroke="#7f8c98"/>
    </svg>
  </div>
</section>

<section class="slide slide--list">
  <div class="ribbons ribbons--right" role="img" aria-label="Flowing blue ribbon decoration"></div>
  <div class="placeholder body-box list-box">
    <ul class="bullets">
      <li>List content</li>
      <li class="sub">Specified list content</li>
    </ul>
    <svg class="insert-icons" width="52" height="34" viewBox="0 0 52 34" aria-hidden="true">
      <rect x="1" y="1" width="14" height="13" fill="#cfdbe6" stroke="#7f97ad"/>
      <rect x="19" y="4" width="4" height="10" fill="#e0803a"/><rect x="24" y="1" width="4" height="13" fill="#4f8fd0"/><rect x="29" y="6" width="4" height="8" fill="#8fbf4a"/>
      <rect x="37" y="2" width="14" height="12" fill="#b9d89a" stroke="#7aa55a"/>
      <rect x="1" y="19" width="14" height="13" fill="#d6e6f3" stroke="#7f97ad"/>
      <rect x="19" y="19" width="14" height="13" fill="#e9d48a" stroke="#a99450"/>
      <circle cx="44" cy="26" r="6" fill="#c9d3dc" stroke="#7f8c98"/>
    </svg>
  </div>
</section>

<section class="slide slide--closing">
  <div class="ribbons ribbons--left" role="img" aria-label="Flowing blue ribbon decoration"></div>
  <h1 class="thanks">THANK YOU!</h1>
  <div class="placeholder body-box closing-box">
    Final words, picture, etc
    <svg class="insert-icons" width="52" height="34" viewBox="0 0 52 34" aria-hidden="true">
      <rect x="1" y="1" width="14" height="13" fill="#cfdbe6" stroke="#7f97ad"/>
      <rect x="19" y="4" width="4" height="10" fill="#e0803a"/><rect x="24" y="1" width="4" height="13" fill="#4f8fd0"/><rect x="29" y="6" width="4" height="8" fill="#8fbf4a"/>
      <rect x="37" y="2" width="14" height="12" fill="#b9d89a" stroke="#7aa55a"/>
      <rect x="1" y="19" width="14" height="13" fill="#d6e6f3" stroke="#7f97ad"/>
      <rect x="19" y="19" width="14" height="13" fill="#e9d48a" stroke="#a99450"/>
      <circle cx="44" cy="26" r="6" fill="#c9d3dc" stroke="#7f8c98"/>
    </svg>
  </div>
  <div class="brand brand--small"><span class="brand__dot"></span>NORVANE</div>
</section>

</body>
</html>
```